One Page Brochure for Metal Recycling Company

We are a scrap metal recycling company and is looking for a one page, one sided brochure A4 size for our upcoming marketing campaign.

This brochure will be mass send to alot of prospective client and we would like it to be professional, but clear, simple and engaging.

We would like to have information on the brochure mainly 1) the type of materials we buy and 2) the service we provide

1) Material
- Scrap Aluminium
- Scrap Stainless Steel
- Scrap Alloy
- Scrap Copper / Brass
- Scrap Iron
- Obselete/Scrap Machinery
- Surplus Material

2) Service
- Prompt & Immediate Payment
- On site weighing
- Free Collection
- Free bin for disposal
- Waste disposal

Etc etc.

Our website is www.tanbokleong.com

Attached our logo and also our previous brochure design for reference.

Target Market(s)

Industrial customer

Industry/Entity Type

It Company

Requirements
Must have
• Our products and our services provide

```html
<!DOCTYPE html>
<html lang="en">
<head>
<meta charset="utf-8">
<title>Tan Bok Leong Recycling – Brochure</title>
<link href="https://fonts.googleapis.com/css2?family=Montserrat:wght@400;500;600;800;900&family=Lato:wght@300;400&family=Oswald:wght@500&display=swap" rel="stylesheet">
<style>
  :root{
    --gold:#c9961f;
    --gold-light:#f2d98c;
    --gold-deep:#a87812;
    --ink:#151515;
    --charcoal:#1d1d1d;
    --grey-text:#4a4a4a;
    --white:#ffffff;
    --stage:#e4e4e4;
  }
  *{margin:0;padding:0;box-sizing:border-box}
  html,body{width:1200px;height:1200px;overflow:hidden;background:var(--stage)}
  .brochure{
    position:absolute;left:194px;top:30px;width:871px;height:1224px;
    transform:scale(0.931);transform-origin:0 0;overflow:hidden;background:var(--white);
    font-family:"Montserrat",sans-serif;
  }
  .artwork{position:absolute;inset:0}
  .brand{position:absolute;left:46px;top:48px;width:300px;text-align:center}
  .brand-mark{width:22px;height:22px;background:var(--gold);margin:0 auto 60px}
  .brand-name{font-weight:800;font-size:28px;letter-spacing:2px;color:var(--gold);line-height:1}
  .brand-sub{font-weight:800;font-size:16px;letter-spacing:2px;color:var(--gold);text-align:right;margin-top:6px;padding-right:8px}
  .headline{position:absolute;left:35px;top:282px}
  .headline-top{font-family:"Lato",sans-serif;font-weight:300;font-size:36px;color:var(--grey-text);line-height:1}
  .headline-main{font-weight:900;font-size:63px;color:var(--gold);line-height:1;margin-top:2px;letter-spacing:1px}
  .headline-sub{font-family:"Lato",sans-serif;font-weight:400;font-size:46px;color:var(--ink);line-height:1;margin-top:2px}
  .info{position:absolute;left:44px;top:494px;color:var(--white)}
  .info-title{font-weight:600;font-size:26px;color:var(--gold);margin:0 0 12px 21px}
  .info-list{list-style:none;margin-bottom:22px}
  .info-list li{font-size:18px;font-weight:500;line-height:30px;position:relative;padding-left:21px}
  .info-list li::before{content:"";position:absolute;left:1px;top:11px;width:9px;height:9px;border-radius:50%;background:var(--gold)}
  .offers{position:absolute;left:57px;top:930px}
  .offer{font-family:"Oswald",sans-serif;font-weight:500;font-size:31px;color:var(--gold);line-height:1;letter-spacing:0.3px}
  .offer-rule{width:252px;height:1px;background:var(--gold-light);margin:12px 0 16px}
  .website{position:absolute;left:46px;top:1155px;display:flex;align-items:center;gap:8px;font-weight:600;font-size:24px;letter-spacing:4px;color:var(--ink)}
</style>
</head>
<body>
<main class="brochure">
  <svg class="artwork" viewBox="0 0 871 1224" width="871" height="1224" aria-hidden="false">
    <defs>
      <linearGradient id="goldSheen" x1="0" y1="0" x2="1" y2="1">
        <stop offset="0" stop-color="#a87812"/><stop offset="0.45" stop-color="#f5dc92"/><stop offset="0.7" stop-color="#d9a632"/><stop offset="1" stop-color="#a87812"/>
      </linearGradient>
      <linearGradient id="goldBand" x1="0" y1="0" x2="1" y2="0">
        <stop offset="0" stop-color="#d7a12a"/><stop offset="0.5" stop-color="#f6e2a6"/><stop offset="1" stop-color="#d39a22"/>
      </linearGradient>
      <linearGradient id="greyBand" x1="0" y1="0" x2="1" y2="0">
        <stop offset="0" stop-color="#e6e6e6"/><stop offset="1" stop-color="#fafafa"/>
      </linearGradient>
      <linearGradient id="brassPhoto" x1="0" y1="0" x2="1" y2="1">
        <stop offset="0" stop-color="#6d6a3c"/><stop offset="0.5" stop-color="#c9b877"/><stop offset="1" stop-color="#5d5833"/>
      </linearGradient>
      <radialGradient id="cablePhoto" cx="0.55" cy="0.45" r="0.7">
        <stop offset="0" stop-color="#6b4c3c"/><stop offset="0.5" stop-color="#2b3130"/><stop offset="1" stop-color="#151a19"/>
      </radialGradient>
      <linearGradient id="copperPhoto" x1="0" y1="0" x2="1" y2="1">
        <stop offset="0" stop-color="#4a2a1a"/><stop offset="0.45" stop-color="#b0694a"/><stop offset="1" stop-color="#3a2116"/>
      </linearGradient>
      <linearGradient id="stripPhoto" x1="0" y1="0" x2="1" y2="1">
        <stop offset="0" stop-color="#8c7d5f"/><stop offset="0.5" stop-color="#c7b48c"/><stop offset="1" stop-color="#4e463a"/>
      </linearGradient>
    </defs>

    <rect class="panel-dark" x="0" y="448" width="871" height="776" fill="var(--charcoal)"/>
    <rect class="headline-band" x="0" y="255" width="871" height="190" fill="url(#greyBand)"/>
    <rect x="0" y="249" width="500" height="5" fill="var(--gold)"/>
    <rect x="0" y="443" width="640" height="5" fill="var(--gold)"/>

    <polygon points="280,0 470,190 490,190 300,0" fill="url(#goldSheen)"/>
    <g role="img" aria-label="Photo of brass scrap offcuts">
      <polygon points="322,0 700,0 510,190" fill="url(#brassPhoto)"/>
    </g>

    <polygon points="470,262 736,0 760,8 500,262" fill="url(#goldSheen)"/>
    <g role="img" aria-label="Photo of cut copper power cables">
      <polygon points="478,274 748,14 871,130 871,420 753,554" fill="url(#cablePhoto)"/>
    </g>

    <polygon points="758,514 871,514 871,860 820,889 758,889" fill="url(#goldSheen)"/>
    <polygon points="810,870 830,860 871,900 871,940" fill="url(#goldSheen)"/>
    <polygon points="410,638 600,458 618,462 428,648" fill="url(#goldSheen)"/>

    <polygon points="404,672 623,456 832,672 618,884" fill="var(--white)"/>
    <g role="img" aria-label="Photo of tangled copper wire scrap">
      <polygon points="412,672 623,464 824,672 618,876" fill="url(#copperPhoto)"/>
    </g>

    <polygon points="660,830 871,1040 871,1090 640,860" fill="url(#goldSheen)"/>

    <polygon points="0,1059 560,1136 590,1224 0,1224" fill="var(--white)"/>
    <polygon points="0,1104 588,1224 0,1224" fill="url(#goldBand)"/>

    <polygon points="394,1014 623,840 827,1024 630,1224 590,1224" fill="var(--white)"/>
    <g role="img" aria-label="Photo of stacked brass and steel strip scrap">
      <polygon points="402,1014 623,848 819,1024 620,1224 594,1224" fill="url(#stripPhoto)"/>
    </g>
    <polygon points="830,1030 871,990 871,1060 680,1224 640,1224" fill="url(#goldSheen)"/>
  </svg>

  <header class="brand">
    <div class="brand-mark"></div>
    <div class="brand-name">TAN BOK LEONG</div>
    <div class="brand-sub">RECYCLING</div>
  </header>

  <section class="headline">
    <p class="headline-top">YOUR ONE STOP SCRAP</p>
    <h1 class="headline-main">SOLUTIONS</h1>
    <p class="headline-sub">your trusted partner</p>
  </section>

  <section class="info">
    <h2 class="info-title">Material</h2>
    <ul class="info-list">
      <li>Scrap Aluminium</li>
      <li>Scrap Stainless Steel</li>
      <li>Scrap Alloy</li>
      <li>Scrap Copper / Brass</li>
      <li>Scrap Iron</li>
      <li>Obselete/Scrap Machinery</li>
      <li>Surplus Material</li>
    </ul>
    <h2 class="info-title">Service</h2>
    <ul class="info-list">
      <li>Prompt &amp; Immediate Payment</li>
      <li>On site weighing</li>
      <li>Waste disposal</li>
    </ul>
  </section>

  <section class="offers">
    <p class="offer">FREE BIN FOR DISPOSAL</p>
    <div class="offer-rule"></div>
    <p class="offer">FREE COLLECTION</p>
  </section>

  <footer class="website">
    <svg width="16" height="16" viewBox="0 0 16 16" aria-hidden="true">
      <circle cx="8" cy="8" r="7" fill="none" stroke="var(--ink)" stroke-width="1.6"/>
      <ellipse cx="8" cy="8" rx="3" ry="7" fill="none" stroke="var(--ink)" stroke-width="1.3"/>
      <line x1="1" y1="8" x2="15" y2="8" stroke="var(--ink)" stroke-width="1.3"/>
    </svg>
    <span>www.tanbokleong.com</span>
  </footer>
</main>
</body>
</html>
```